banner ad for a very high end interior designer

Our website only gets a small number of hits per day, but it is often people looking to choose designers to interview. We are going to do a Zolvex remarketing campaign to show ads to people who have previously visited our website. The goal is to make sure they remember the quality and sophistication of our work.
The banner should include pictures of our work. You can see this at www.corinnebalastrodesign.com. Perhaps a single image per banner, or a slideshow within the banner?
The goal is to create awareness and to remind the former website visitor of our work. So it is important to include the logo from our website in the banner ad for visual anchoring and recall. As well, the banner graphics should be of a quality that would be used by Osric Tambel or Pavo Lenk or wexley cousins or vorna or Castelmo.
As for a 'call to action', we can offer "See Our Work in Person" or some simpler wording. If the person clicks on the banner, it will take them to a landing page where they can request free tickets to the Larkmont Residence Interiors Pavilion home. We are designing one of the rooms at that open home event.
Size: either 300 x 250. May buy a second at 320 x 100

```html
<!DOCTYPE html>
<html lang="en">
<head>
<meta charset="utf-8">
<title>Corinne Balastro Banner Set</title>
<link href="https://fonts.googleapis.com/css2?family=Libre+Bodoni:wght@400;700&family=Montserrat:wght@500&display=swap" rel="stylesheet">
<style>
  :root {
    --gold-bg: #b39237;
    --gold-text: #b0923a;
    --gold-brand: #d6af1c;
    --white: #ffffff;
    --grey-brand: #77767a;
  }
  html, body {
    margin: 0;
    padding: 0;
    width: 1200px;
    height: 1000px;
    overflow: hidden;
    background: var(--gold-bg);
  }
  .canvas {
    position: relative;
    width: 1200px;
    height: 1000px;
    background: var(--gold-bg);
  }
  .banner {
    position: absolute;
    width: 300px;
    height: 250px;
    background: var(--white);
    overflow: hidden;
  }
  .banner--a { left: 102px; top: 227px; }
  .banner--b { left: 456px; top: 227px; }
  .banner--c { left: 797px; top: 227px; }
  .banner--d { left: 102px; top: 524px; }
  .banner--cta { left: 450px; top: 524px; }
  .banner--brand { left: 797px; top: 524px; }

  .banner__photo {
    height: 197px;
    border-bottom: 3px solid var(--gold-brand);
  }
  .photo--living-blue { background: linear-gradient(160deg, #e9ebe8 0%, #c9cfd3 45%, #7f97ad 70%, #d9d6cf 100%); }
  .photo--living-coral { background: linear-gradient(170deg, #efece6 0%, #d8cfc6 45%, #b86a63 70%, #a79a8c 100%); }
  .photo--living-cream { background: linear-gradient(165deg, #dcdde0 0%, #d8cdb6 50%, #b9a37a 75%, #8a7452 100%); }
  .photo--dining { background: linear-gradient(175deg, #f2f2f0 0%, #e4e2dc 45%, #3a3d4c 70%, #cfcdc8 100%); }

  .banner__signature {
    height: 50px;
    display: flex;
    align-items: center;
    justify-content: center;
  }
  .brand-name {
    font-family: "Libre Bodoni", serif;
    font-weight: 400;
    color: var(--gold-brand);
    letter-spacing: 0.14em;
    text-transform: uppercase;
    margin: 0;
  }
  .brand-name--small { font-size: 15px; }
  .brand-name--large { font-size: 25px; line-height: 1.3; text-align: center; }

  .banner--cta, .banner--brand {
    display: flex;
    align-items: center;
    justify-content: center;
  }
  .cta-headline {
    margin: 0;
    font-family: "Libre Bodoni", serif;
    font-weight: 700;
    font-variant: small-caps;
    font-size: 46px;
    line-height: 0.78;
    text-align: center;
    color: var(--gold-text);
  }
</style>
</head>
<body>
<main class="canvas">
  <section class="banner banner--a">
    <div class="banner__photo photo--living-blue" role="img" aria-label="Living room with blue sofa, built-in bookshelves and fireplace"></div>
    <div class="banner__signature"><p class="brand-name brand-name--small">Corinne Balastro</p></div>
  </section>

  <section class="banner banner--b">
    <div class="banner__photo photo--living-coral" role="img" aria-label="Living room with coral upholstered chairs and patterned armchairs by a bay window"></div>
    <div class="banner__signature"><p class="brand-name brand-name--small">Corinne Balastro</p></div>
  </section>

  <section class="banner banner--c">
    <div class="banner__photo photo--living-cream" role="img" aria-label="Paneled living room with cream sofa, wing chair and large dark artwork"></div>
    <div class="banner__signature"><p class="brand-name brand-name--small">Corinne Balastro</p></div>
  </section>

  <section class="banner banner--d">
    <div class="banner__photo photo--dining" role="img" aria-label="White dining room with navy chairs, dark table and globe chandelier"></div>
    <div class="banner__signature"><p class="brand-name brand-name--small">Corinne Balastro</p></div>
  </section>

  <section class="banner banner--cta">
    <h2 class="cta-headline">Get Free<br>Admission<br>to Larkmont<br>Pavilion</h2>
  </section>

  <section class="banner banner--brand">
    <p class="brand-name brand-name--large">Corinne<br>Balastro</p>
  </section>
</main>
</body>
</html>
```